Jazz Album Art for New Live Recording Release

Looking for a creative and experienced graphic designer to create album art for my song “Night Ramblin’.” This track was originally released in 2020, and I am now preparing to release a special live recording from my 40th birthday party. The album art will be used on various streaming platforms, including Lumen Tunes, Wavelo, and more.

Requirements:

1. Theme and Style: The design should embody the essence of the song “Night Ramblin’.” It should convey a sense of fun, energy, and nostalgia, reflecting the celebratory mood of a 40th birthday party. The style can be vibrant and colorful, capturing the essence of a live, joyful celebration.
2. Text Elements: The design must include the song title “Night Ramblin’” and the text “Live from the Birthday Party” and my name “Dorin Mackesy.” Feel free to experiment with typography and placement, but ensure that the text is legible across various device sizes.
3. Imagery: While I am open to creative interpretations, the imagery should resonate with the themes of music, celebration, and liveliness. Whether you choose to go abstract or literal, the artwork should capture the viewer’s attention and reflect the spirit of the song.
4. Format and Dimensions: The final design should be square, with a minimum resolution of 3000x3000 pixels, to ensure it looks great on all streaming platforms. The artwork should also be adaptable to smaller sizes without losing its visual appeal.
5. File Requirements: Please submit the final design in both .jpeg and .png formats. Ensure that the .png file has a transparent background.

Nice to have:
1. Use branding elements (colors, text types, logo, or themes) from my website dorinm.net

2. Incorporate image attached

Target Market(s)

Live Jazz Music Lovers

Industry/Entity Type

Music / Entertainment

Requirements
Must have
• Requirements: 1. Theme and Style: The design should embody the essence of the song “Night Ramblin’.” It should convey a sense of fun, energy, and nostalgia, reflecting the celebratory mood of a 40th birthday party. The style can be vibrant and colorful, capturing the essence of a live, joyful celebration. 2. Text Elements: The design must include the song title “Night Ramblin’” and the text “Live from the 40th Birthday Party.” Feel free to experiment with typography and placement, but ensure that the text is legible across various device sizes. 3. Imagery: While I am open to creative interpretations, the imagery should resonate with the themes of music, celebration, and liveliness. Whether you choose to go abstract or literal, the artwork should capture the viewer’s attention and reflect the spirit of the song. 4. Format and Dimensions: The final design should be square, with a minimum resolution of 3000x3000 pixels, to ensure it looks great on all streaming platforms. The artwork should also be adaptable to smaller sizes without losing its visual appeal. 5. File Requirements: Please submit the final design in both .jpeg and .png formats. Ensure that the .png file has a transparent background.
Nice to have
• Nice to have: 1. Use branding elements (colors, text types, logo, or themes) from my website dorinm.net 2. Incorporate image attached
Should not have
• NA

```html
<!DOCTYPE html>
<html lang="en">
<head>
<meta charset="utf-8">
<title>Night Ramblin’ – Live Cover Options</title>
<link rel="stylesheet" href="https://fonts.googleapis.com/css2?family=Jost:wght@300;400;600;700&family=Kaushan+Script&display=swap">
<style>
  :root {
    --page: #ffffff;
    --ink: #ffffff;
    --rec-red: #e5202a;
    --blue: #3953a6;
    --violet: #6a5aa9;
    --orchid: #c98abc;
    --floor: #cf82bf;
    --plum: #7b3a77;
    --plum-deep: #5a2a5e;
    --night: #140e26;
  }
  * { margin: 0; padding: 0; box-sizing: border-box; }
  html, body { width: 1200px; height: 661px; overflow: hidden; background: var(--page); }
  .board { position: relative; width: 1200px; height: 661px; }

  .cover {
    position: absolute;
    top: 81px;
    width: 504px;
    height: 504px;
    overflow: hidden;
    color: var(--ink);
    font-family: "Jost", sans-serif;
    background:
      radial-gradient(ellipse 260px 70px at 240px 490px, var(--floor) 0%, rgba(207,130,191,0.75) 45%, rgba(207,130,191,0) 100%),
      radial-gradient(circle 230px at 410px 20px, var(--orchid) 0%, rgba(201,138,188,0.55) 45%, rgba(201,138,188,0) 100%),
      linear-gradient(115deg, var(--blue) 0%, var(--blue) 30%, var(--violet) 60%, #8d6db3 100%);
  }
  .cover--framed { left: 82px; }
  .cover--script { left: 622px; }
  .cover--script::after {
    content: "";
    position: absolute;
    inset: 0;
    background:
      radial-gradient(ellipse 330px 150px at 0px 504px, rgba(20,14,38,0.95) 0%, rgba(20,14,38,0.55) 45%, rgba(20,14,38,0) 100%),
      linear-gradient(180deg, rgba(20,14,38,0) 60%, rgba(20,14,38,0.35) 85%, rgba(20,14,38,0) 100%);
    pointer-events: none;
    z-index: 1;
  }

  .performer-photo {
    position: absolute;
    left: 204px;
    top: 20px;
    width: 212px;
    height: 468px;
    border-radius: 45% 45% 20% 20% / 20% 20% 8% 8%;
    background: radial-gradient(ellipse at 50% 45%, var(--plum) 0%, rgba(123,58,119,0.85) 50%, rgba(90,42,94,0) 100%);
    z-index: 2;
  }

  .title {
    position: absolute;
    left: 37px;
    top: 34px;
    z-index: 3;
    line-height: 1;
  }
  .title__line { display: block; font-weight: 600; }
  .title__line--top { font-size: 53px; line-height: 48px; letter-spacing: -0.5px; }
  .title__line--main { font-size: 55px; line-height: 50px; letter-spacing: -0.5px; }
  .title__artist { display: block; font-weight: 400; font-size: 23px; margin-top: 6px; }

  .live-tag {
    display: flex;
    align-items: center;
    gap: 6px;
    font-weight: 400;
  }
  .live-tag::before {
    content: "";
    width: 14px;
    height: 14px;
    border-radius: 50%;
    background: var(--rec-red);
  }

  .event-frame {
    position: absolute;
    left: 42px;
    top: 241px;
    width: 231px;
    height: 132px;
    z-index: 3;
  }
  .event-frame svg { position: absolute; inset: 0; }
  .event-frame .live-tag { position: absolute; left: 49px; top: 20px; font-size: 19px; }
  .event-frame__name {
    position: absolute;
    left: 0;
    width: 231px;
    top: 43px;
    text-align: center;
    font-weight: 300;
    font-size: 42px;
    line-height: 41px;
  }

  .event-script { position: absolute; left: 43px; top: 0; z-index: 3; }
  .event-script .live-tag { position: absolute; left: 71px; top: 266px; font-size: 22px; white-space: nowrap; }
  .event-script .live-tag::before { width: 16px; height: 16px; }
  .event-script__word {
    position: absolute;
    font-family: "Kaushan Script", cursive;
    font-size: 52px;
    white-space: nowrap;
    line-height: 1;
  }
  .event-script__word--first { left: 0; top: 300px; }
  .event-script__word--second { left: 80px; top: 356px; }

  .artist-mark {
    position: absolute;
    left: 46px;
    top: 434px;
    z-index: 3;
    font-weight: 400;
    font-size: 24px;
    letter-spacing: 1px;
    white-space: nowrap;
  }
  .cover--script .artist-mark { left: 50px; }
</style>
</head>
<body>
<main class="board">

  <section class="cover cover--framed">
    <div class="performer-photo" role="img" aria-label="Photo of the saxophonist in a plum suit playing on stage"></div>
    <h1 class="title">
      <span class="title__line title__line--top">Night</span>
      <span class="title__line title__line--main">Ramblin’</span>
      <span class="title__artist">with Dorin Mackesy</span>
    </h1>
    <div class="event-frame">
      <svg width="231" height="132" viewBox="0 0 231 132" fill="none" stroke="#fff" stroke-width="1.6">
        <polyline points="1,46 1,1 46,1"/>
        <polyline points="186,1 230,1 230,46"/>
        <polyline points="1,86 1,131 46,131"/>
        <polyline points="186,131 230,131 230,86"/>
      </svg>
      <p class="live-tag">Live from the</p>
      <p class="event-frame__name">Birthday<br>Party</p>
    </div>
    <p class="artist-mark">DORIN M.</p>
  </section>

  <section class="cover cover--script">
    <div class="performer-photo" role="img" aria-label="Photo of the saxophonist in a plum suit playing on stage"></div>
    <h1 class="title">
      <span class="title__line title__line--top">Night</span>
      <span class="title__line title__line--main">Ramblin’</span>
      <span class="title__artist">with Dorin Mackesy</span>
    </h1>
    <div class="event-script">
      <p class="live-tag">Live from the</p>
      <p class="event-script__word event-script__word--first">Birthday</p>
      <p class="event-script__word event-script__word--second">Party</p>
    </div>
    <p class="artist-mark">DORIN M.</p>
  </section>

</main>
</body>
</html>
```